Webdesign für Naturheilpraktiker gesucht
Zielgruppe
Ich arbeite im Gesundheitswesen als Naturheilpraktiker Traditionell Tibetische Medizin.
Verfüge aber über verschiedene Anwendungstechniken.
Die Zielgruppe sind alle Menschen die mehr als nur klassische Medizin wollen, die mit der klassischen Schulmedizin nicht mehr weiter kommen und einen alternativen Weg suchen. Menschen die neben der Schulmedizin noch einen anderen Weg suchen.
Menschen im Wellness und Fitnessbereich.
Ernährungsbewusste Menschen.
Sportler allgemein da ich über eine neue Technik verfüge (KERVO) die erst auf den Markt kommt und mit der verschiedene Beschwerden gelindert werden können.
Grob gesagt alles was mit Medizin, Komplementärmedizin, Gesundheit, Wellness, Sport usw zu tun hat.
Kompetenzen der Traditionell Tibetische Medizin:
- Massage als Gesundheitssystem oder als Wellness
- Ernährungsberatung
- tibetisches Yoga
- Lebensberatung
- Familienstellen
Aufgabenstellung
Der Firmennamen und das Logo bestehen.
In der Tradition der tibetischen Medizin ist vor allem Blau (Medizin Buddha) die Farben sind aber frei wählbar.
Es soll Vertrautheit, Geborgenheit und Wärme ausstrahlen.
Nicht zu feminin erscheinen.
Einfach ein paar Ideen
http://massagepraxis-wolfrin.example
http://www.himalheilkunde.example

```html
<!DOCTYPE html>
<html lang="de">
<head>
<meta charset="utf-8">
<title>Lotusweg – Traditionell Tibetische Medizin</title>
<link href="https://fonts.googleapis.com/css2?family=Roboto:wght@400;500;700;900&family=Lobster&display=swap" rel="stylesheet">
<style>
:root{
  --blue:#235998;
  --blue-soft:#6d93bf;
  --green:#46b48c;
  --white:#ffffff;
  --ink:#333333;
  --hero-a:#6f8f45;
  --hero-b:#9db44a;
  --hero-c:#5c7a52;
}
*{box-sizing:border-box;margin:0;padding:0}
html,body{width:721px;height:1200px;overflow:hidden;background:var(--white);font-family:"Roboto",sans-serif}
.page{position:relative;width:721px;height:1200px}
.abs{position:absolute}

/* header */
.brand{left:152px;top:6px;width:60px;text-align:center;color:var(--blue);font-size:6px;font-weight:500;letter-spacing:1.5px}
.brand-dot{width:26px;height:26px;border-radius:50%;background:var(--blue);margin:0 auto 4px}
.nav{left:243px;top:24px;display:flex;gap:15px;font-size:5.6px;font-weight:500;color:var(--blue)}
.nav span{padding-bottom:7px}
.nav .active{border-bottom:1.2px solid var(--blue);padding:0 7px 7px}
.contact{right:153px;top:16px;text-align:right;font-size:5.2px;font-weight:500;color:var(--blue);line-height:11.5px}
.contact svg{vertical-align:-1px;margin-right:3px}

/* hero */
.hero{left:3px;top:49px;width:715px;height:246px;background:linear-gradient(160deg,var(--hero-b) 0%,var(--hero-a) 40%,var(--hero-c) 75%,#a5a63c 100%)}
.hero-brand{left:0;top:73px;width:721px;text-align:center;color:var(--white);font-size:9px;letter-spacing:3px;font-weight:500}
.hero-brand .ring{width:60px;height:60px;border:2px solid var(--white);border-radius:50%;margin:0 auto 8px}
.hero-brand small{display:block;font-size:3px;letter-spacing:.5px;margin-top:1px}
.hero-title{left:0;top:164px;width:721px;text-align:center;color:var(--white);font-family:"Lobster",cursive;font-size:35px}
.hero-sub{left:97px;top:210px;color:var(--white);font-size:14.5px;font-weight:700;line-height:14px}
.hero-sub span{display:block;padding-left:75px}

/* service cards */
.services{left:41px;top:314px;display:flex;gap:4px}
.service{width:156px;height:141px;background:var(--blue);color:var(--white);text-align:center;padding-top:19px}
.service .icon{width:26px;height:26px;border-radius:50%;background:var(--white);margin:0 auto 14px;display:flex;align-items:center;justify-content:center}
.service h3{font-size:6.6px;font-weight:500;margin-bottom:9px}
.service p{font-size:5px;line-height:9.5px;padding:0 16px;margin-bottom:7px}
.service a{font-size:4.8px;font-weight:700}

/* news band */
.band{left:3px;top:474px}
.news-kicker{left:0;top:506px;width:721px;text-align:center;color:var(--white);font-size:15px;font-weight:700}
.news-title{left:0;top:527px;width:721px;text-align:center;color:var(--white);font-size:24px;font-weight:900}
.feature{left:169px;top:562px;width:383px;height:125px;background:var(--white);display:flex}
.feature-photo{width:111px;height:125px;background:linear-gradient(135deg,#9aa8bd 0%,#c89a3c 45%,#e8b62a 60%,#7f8ea8 100%)}
.feature-body{padding:18px 0 0 15px;width:180px;color:var(--ink)}
.feature-body h4{font-size:8px;font-weight:500;letter-spacing:.4px;margin-bottom:8px}
.feature-body p{font-size:5.4px;line-height:10.2px;margin-bottom:7px}
.feature-btn{position:absolute;left:307px;top:55px;width:63px;height:14px;border-radius:7px;background:var(--green);color:var(--white);font-size:5.2px;font-weight:700;text-align:center;line-height:14px}

/* testimonials */
.t-head{left:0;top:778px;width:721px;text-align:center;color:var(--blue);font-size:15px;font-weight:700}
.quotes{left:146px;top:817px;display:flex;gap:10.5px}
.quote{position:relative;width:136px}
.quote-box{height:66px;background:var(--blue);color:var(--white);font-size:6px;line-height:12px;padding:9px 20px}
.quote-box::after{content:"";position:absolute;left:30px;top:66px;border:3px solid transparent;border-top-color:var(--blue)}
.person{display:flex;align-items:center;gap:6px;margin:19px 0 0 21px;color:var(--blue);font-size:7.5px;font-weight:500}
.avatar{width:24px;height:24px;border-radius:50%;background:linear-gradient(160deg,#c9a58e,#5a3c30)}
.dot{left:359px;top:932px;width:3px;height:3px;border-radius:50%;background:#111}

/* footer */
.footer{left:0;top:979px;width:721px;height:203px;background:var(--blue-soft);color:var(--white)}
.f-brand{left:150px;top:32px;width:96px;text-align:center;color:var(--blue);font-size:8px;font-weight:500;letter-spacing:2.5px}
.f-brand .ring{width:48px;height:48px;border-radius:50%;background:var(--blue);margin:0 auto 8px}
.f-text{left:150px;top:110px;width:104px;font-size:5px;line-height:9.4px}
.socials{left:150px;top:160px;display:flex;gap:4px}
.socials span{width:12px;height:12px;background:rgba(255,255,255,.25)}
.legal{left:293px;top:32px;font-size:5px;line-height:11px}
.legal h5{font-size:6.5px;font-weight:500;margin-bottom:5px}
.form{left:398px;top:33px;width:173px;font-size:4.8px;font-weight:500}
.form h5{font-size:7px;font-weight:700;margin-bottom:6px}
.form label{display:block;margin-bottom:3px}
.field{background:var(--white);color:#8aa;font-weight:400;height:15px;padding:4px 5px;margin-bottom:6px}
.field.big{height:36px}
.send{background:var(--blue);text-align:center;height:15px;line-height:15px;font-weight:700;letter-spacing:.5px}
.bottom{left:0;top:1182px;width:721px;height:18px;background:var(--blue);color:var(--white);font-size:4.5px;padding:7px 0 0 150px}
</style>
</head>
<body>
<div class="page">

  <header>
    <div class="abs brand"><div class="brand-dot"></div>LOTUSWEG</div>
    <nav class="abs nav">
      <span class="active">Home</span><span>Über mich</span><span>Die Naturheilpraxis</span><span>Angebote ▾</span><span>Kontakt</span>
    </nav>
    <div class="abs contact">
      <div><svg width="7" height="7" viewBox="0 0 24 24"><path fill="#235998" d="M6.6 10.8a15 15 0 0 0 6.6 6.6l2.2-2.2c.3-.3.7-.4 1-.2 1.1.4 2.3.6 3.6.6.6 0 1 .4 1 1V20c0 .6-.4 1-1 1A17 17 0 0 1 3 4c0-.6.4-1 1-1h3.5c.6 0 1 .4 1 1 0 1.3.2 2.5.6 3.6.1.3 0 .7-.2 1z"/></svg>+49 000 555 0147</div>
      <div><svg width="10" height="8" viewBox="0 0 24 20"><path fill="#235998" d="M2 7l10-6 10 6v11H2z"/><path fill="#fff" d="M4 8l8 5 8-5"/></svg>mail[at]lotusweg.example</div>
    </div>
  </header>

  <section>
    <div class="abs hero" role="img" aria-label="Foto: grüne Reisterrassen mit Holzhütte im Nebel"></div>
    <div class="abs hero-brand"><div class="ring"></div>LOTUSWEG<small>NATURHEILPRAXIS TRADITIONELL TIBETISCHE MEDIZIN</small></div>
    <h1 class="abs hero-title">Traditionell Tibetische Medizin</h1>
    <p class="abs hero-sub">MASSAGE | ERNÄHRUNG | TIBETISCHES YOGA<span>LEBENSBERATUNG | FAMILIENSTELLEN</span></p>
  </section>

  <section class="abs services">
    <div class="service"><div class="icon"><svg width="13" height="13" viewBox="0 0 24 24"><path fill="#235998" d="M12 2l3 7h7l-5.5 4.5 2 7.5L12 16.5 5.5 21l2-7.5L2 9h7z"/></svg></div><h3>MASSAGE</h3><p>Lorem ipsum dolor sit amet, consectetur adipiscing elit. Ut elit tellus, luctus nec ullamcorper mattis, pulvinar dapibus leo.</p><a>MEHR INFORMATION</a></div>
    <div class="service"><div class="icon"><svg width="13" height="13" viewBox="0 0 24 24"><path fill="#235998" d="M12 2l3 7h7l-5.5 4.5 2 7.5L12 16.5 5.5 21l2-7.5L2 9h7z"/></svg></div><h3>ERNÄHRUNG</h3><p>Lorem ipsum dolor sit amet, consectetur adipiscing elit. Ut elit tellus, luctus nec ullamcorper mattis, pulvinar dapibus leo.</p><a>MEHR INFORMATION</a></div>
    <div class="service"><div class="icon"><svg width="13" height="13" viewBox="0 0 24 24"><path fill="#235998" d="M12 2l3 7h7l-5.5 4.5 2 7.5L12 16.5 5.5 21l2-7.5L2 9h7z"/></svg></div><h3>YOGA</h3><p>Lorem ipsum dolor sit amet, consectetur adipiscing elit. Ut elit tellus, luctus nec ullamcorper mattis, pulvinar dapibus leo.</p><a>MEHR INFORMATION</a></div>
    <div class="service"><div class="icon"><svg width="13" height="13" viewBox="0 0 24 24"><path fill="#235998" d="M12 2l3 7h7l-5.5 4.5 2 7.5L12 16.5 5.5 21l2-7.5L2 9h7z"/></svg></div><h3>LEBENSBERATUNG</h3><p>Lorem ipsum dolor sit amet, consectetur adipiscing elit. Ut elit tellus, luctus nec ullamcorper mattis, pulvinar dapibus leo.</p><a>MEHR INFORMATION</a></div>
  </section>

  <section>
    <svg class="abs band" width="715" height="274" viewBox="0 0 715 274"><polygon points="0,16 715,0 715,259 0,273" fill="#46b48c"/></svg>
    <h2 class="abs news-kicker">NEU BEI LOTUSWEG</h2>
    <h2 class="abs news-title">KERVO</h2>
    <article class="abs feature">
      <div class="feature-photo" role="img" aria-label="Foto: Ringelblumen und Teeglas auf Jute"></div>
      <div class="feature-body">
        <h4>BEHANDLUNG MIT KERVO</h4>
        <p>Lorem ipsum dolor sit amet, consectetur adipiscing elit. Ut elit tellus, luctus nec ullamcorper mattis, pulvinar dapibus leo.</p>
        <p>Lorem ipsum dolor sit amet, consectetur adipiscing elit. Ut elit tellus, luctus nec ullamcorper mattis, pulvinar dapibus leo.</p>
      </div>
      <div class="feature-btn">MEHR ERFAHREN</div>
    </article>
  </section>

  <section>
    <h2 class="abs t-head">MENSCHEN DENEN WIR HELFEN KONNTEN</h2>
    <div class="abs quotes">
      <div class="quote"><div class="quote-box">Lorem ipsum dolor sit amet, consectetur adipiscing elit. Ut elit tellus, luctus nec ullamcorper mattis, pulvinar dapibus leo.</div><div class="person"><div class="avatar" role="img" aria-label="Porträtfoto Kundin"></div>Miriam T.</div></div>
      <div class="quote"><div class="quote-box">Lorem ipsum dolor sit amet, consectetur adipiscing elit. Ut elit tellus, luctus nec ullamcorper mattis, pulvinar dapibus leo.</div><div class="person"><div class="avatar" role="img" aria-label="Porträtfoto Kunde"></div>Jonas R.</div></div>
      <div class="quote"><div class="quote-box">Lorem ipsum dolor sit amet, consectetur adipiscing elit. Ut elit tellus, luctus nec ullamcorper mattis, pulvinar dapibus leo.</div><div class="person"><div class="avatar" role="img" aria-label="Porträtfoto Kundin"></div>Lena F.</div></div>
    </div>
    <div class="abs dot"></div>
  </section>

  <footer class="abs footer">
    <div class="abs f-brand"><div class="ring"></div>LOTUSWEG</div>
    <p class="abs f-text">I am text block. Click edit button to change this text. Lorem ipsum dolor sit amet, consectetur adipiscing elit. Ut elit tellus, luctus nec ullamcorper matti pibus leo.</p>
    <div class="abs socials"><span></span><span></span><span></span><span></span><span></span><span></span></div>
    <div class="abs legal"><h5>Rechtliche Angaben</h5><div>Datenschutz</div><div>Impressum</div></div>
    <div class="abs form">
      <h5>KONTAKT</h5>
      <label>Name</label><div class="field">Name</div>
      <label>E-Mail</label><div class="field">E-Mail</div>
      <label>Nachricht</label><div class="field big">Nachricht</div>
      <div class="send">SENDEN</div>
    </div>
  </footer>
  <div class="abs bottom">© Lotusweg 2018</div>

</div>
</body>
</html>
```